Drug Sample Pack Design
Nausea Prevention Drug Packaging
Project: Drug Sample Pack Design
Creative Brief
I need a sample pack design for a new dietary supplement I am producing. I say sample pack, but it's not really a sample, that's how we are going to sell the drug, but it is packaged in the typical foil sample packs you see in stores. This is what I mean: (My favorite, but all four are good) http://www.pelvorasupply.example/images/Ventrolin-BX.gif http://fl2.trovimart.example/files/images/10161/single-dose-corvane-febrilex-10-packs~10160384.jpg http://beta.zembuy.example/img/item/117/499/357/o_mfZsnBHbgIjyxiw.jpg http://www.savingowl.example/blog/wp-content/uploads/2010/10/Fizzora_Tablet_Box.gif My product is called "Gastrelle" and the tagline is "Nausea Prevention for Alcohol Use" Your job is to sell me my product. It is marketed as a dietary supplement, not a drug so any claim you make must be supported by scientific evidence. Ours is, we are Doctor/Physician Approved and have done several Double Blind Clinical Trials "Clinically Approved". Our main competitors are products like Rumbo Max, http://www.rumbomax.example/ and Belvix, Pelks, other antacids. Our product shares the same active ingredient as all of those above, but we are marketing our product differently, for Nausea Prevention, not "Hangover Prevention" or as an "antacid" even though it is the same thing, it must not appear that way. Rumbo looks like something you would buy at a truck stop. It's trashy. Belvix make your kids want to eat them, they are fun, colorful etc... We want to be professional. The ventrolin bx pack I showed above really captures that. We want people to see "Gastrelle" and think, wow, this might actually work. This is professional, I trust this product. It is doctor approved, is has gone through a clinical trial, this looks not only safe, but effective. We think a good way to do that would be to have a diagram on the package depicting how our product works. We suspect the active ingredient of gastrelle, carbonate ion, forms a "protective lining" around the stomach. Normally, alcohol irritates this lining and causes it to produce lots of acid. When acid accumulates in the stomach, you get nauseous and vomit to get rid of the excess acid. Our active ingredient both prevents this irritation and neutralizes the acid, preventing nausea. So maybe have a diagram like this, but obviously this is way to ugly, draw it yourself or find something better, that includes some cartoon of Gastrelle protecting the stomach and/or neurtralizing acid and maybe if you can think of a way, to show that now, since acid is low, the brain is not signaled to throw up/vomit. http://images.lornapedia.example/2342474_com_500pxstoma.png Everything I've said is a suggestion, the winner will be the product that I want to buy the most. Sell me "Gastrelle" The winner will get first offer for all future graphic design for Dietary Supplements from Quillon Industries.
Health
College Students
Suggestions: This product must look professional. See the ventrolin bx image. This must include some sort of Doctor/Physician Approved or Clinically Proven message. Must also include "Nausea Prevention for Alcohol Use" Must include "Dietary Supplement" Include a link to my website, http://gastrelle.example (it isn't up yet) This is a dietary supplement and as such must include the standard ingredients label on the back. The active ingredient is 1000mg Calcium Carbonate per tablet. There are two tablets per package. Two tablets per serving. The diagram is optional, I think it might look good, but it's up to you. While I technically call these requirements, despite whatever I said, the winner will be the package that I want to buy the most. It's as simple as that. If you decide you want to change the name of my product, change my tagline, not do a diagram, completely go against all of my suggestions, but it still sells me the product, that is fine by me. Sell me "Gastrelle"

```html
<!DOCTYPE html>
<html lang="en">
<head>
<meta charset="utf-8">
<title>Gastrelle Mint – Packaging Layouts</title>
<link rel="stylesheet" href="https://fonts.googleapis.com/css2?family=Archivo+Black&family=Arimo:wght@400;700&display=swap">
<style>
  :root{
    --navy:#0b3470;
    --blue:#1462b3;
    --sky:#3f9be0;
    --ice:#e8f3fb;
    --paper:#ffffff;
    --lime:#8cc63f;
    --lime-dark:#5e9a1e;
    --yellow:#f4e21a;
    --red:#d8261c;
    --ink:#1b2a3e;
    --stage:#d9d6d0;
  }
  *{box-sizing:border-box;margin:0;padding:0}
  html,body{width:1200px;height:847px;overflow:hidden}
  body{background:var(--stage);font-family:"Arimo",Arial,sans-serif;color:var(--ink);position:relative}
  .piece{position:absolute;overflow:hidden;box-shadow:0 2px 6px rgba(0,0,0,.25)}
  .brand{font-family:"Archivo Black","Arial Black",sans-serif;color:var(--paper);letter-spacing:1px;line-height:1}
  .kicker{font-weight:700;text-transform:uppercase;letter-spacing:1px;color:var(--paper)}
  .caps{text-transform:uppercase;font-weight:700}
  .checks{font-weight:700;color:var(--navy);text-transform:uppercase;line-height:1.5}
  .checks span{color:var(--lime-dark)}
  .diagram{background:radial-gradient(circle at 50% 45%,#ffffff 0%,#d3e9f8 55%,#8cc3ea 100%);border:3px solid var(--sky);border-radius:50%}
  .mint-art{background:radial-gradient(ellipse at 40% 60%,#ffffff 0%,#e3f2c7 45%,var(--lime) 100%)}
  .url{color:var(--paper);font-weight:700;text-transform:uppercase;letter-spacing:1px}

  /* ---------- carton: top panel ---------- */
  .carton-top{left:120px;top:24px;width:455px;height:108px;background:linear-gradient(var(--navy),var(--blue))}
  .carton-top .kicker{position:absolute;left:24px;top:20px;font-size:11px}
  .carton-top .brand{position:absolute;left:22px;top:38px;font-size:44px}
  .carton-top .stripe{position:absolute;left:0;right:0;bottom:0;height:16px;background:var(--sky)}

  /* ---------- carton: side panel ---------- */
  .carton-side{left:36px;top:132px;width:84px;height:408px;background:linear-gradient(90deg,var(--navy),var(--blue))}
  .carton-side .vert{position:absolute;left:42px;top:140px;transform:translate(-50%,-50%) rotate(-90deg);white-space:nowrap;text-align:center}
  .carton-side .vert .kicker{font-size:9px;display:block}
  .carton-side .vert .brand{font-size:30px}
  .carton-side .foot{position:absolute;left:0;right:0;bottom:0;height:130px}
  .carton-side .foot .mint-art{position:absolute;inset:0}
  .carton-side .foot .tag{position:absolute;left:8px;bottom:10px;transform:rotate(-90deg);transform-origin:left bottom;font-size:14px;font-weight:700;color:var(--navy);white-space:nowrap;margin-left:18px}

  /* ---------- carton: front panel ---------- */
  .front{width:455px;height:323px;background:linear-gradient(var(--paper),var(--ice))}
  .carton-front{left:120px;top:132px}
  .carton-back{left:120px;top:550px;transform:rotate(180deg);height:278px}
  .front .band{position:absolute;left:0;right:0;top:0;height:118px;background:linear-gradient(var(--navy),var(--blue))}
  .front .band .kicker{position:absolute;left:0;right:0;top:16px;text-align:center;font-size:12px}
  .front .band .brand{position:absolute;left:0;right:0;top:38px;text-align:center;font-size:58px}
  .front .band .count{position:absolute;right:18px;top:16px;color:var(--paper);font-weight:700;font-size:18px}
  .front .tagline{position:absolute;left:0;right:0;top:118px;height:26px;background:var(--sky);color:var(--paper);font-size:12px;text-align:center;line-height:26px;letter-spacing:1px}
  .ribbon{position:absolute;left:-30px;top:10px;width:110px;height:24px;background:var(--yellow);color:var(--red);transform:rotate(-40deg);font-weight:700;font-size:13px;text-align:center;line-height:24px;z-index:2}
  .front .tile{position:absolute;left:0;top:144px;width:150px;height:140px;background:var(--lime)}
  .front .tile .mint-art{position:absolute;inset:0}
  .front .tile .tag{position:absolute;left:10px;top:8px;font-size:22px;font-weight:700;color:var(--navy)}
  .front .tile .note{position:absolute;left:0;right:0;bottom:6px;text-align:center;font-size:9px;color:var(--navy);font-weight:700}
  .front .proof{position:absolute;left:172px;top:160px;font-size:20px;color:var(--navy);line-height:1.05}
  .front .checks{position:absolute;left:172px;top:222px;font-size:11px}
  .front .diagram{position:absolute;right:18px;top:150px;width:120px;height:120px}
  .front .foot{position:absolute;left:0;right:0;bottom:0;height:39px;background:var(--navy)}
  .front .foot .url{position:absolute;right:18px;top:12px;font-size:12px}
  .carton-back .tile{height:95px}
  .carton-back .foot{height:30px}
  .carton-back .foot .url{top:8px}
  .carton-back .checks{left:172px;top:170px}
  .carton-back .diagram{width:90px;height:90px;top:150px}

  /* ---------- carton: underside ---------- */
  .carton-base{left:120px;top:455px;width:455px;height:95px;background:var(--paper);border-top:1px solid #c9d6e3;border-bottom:1px solid #c9d6e3}
  .carton-base .copy{position:absolute;left:30px;top:14px;width:260px;font-size:8px;line-height:1.45;transform:rotate(180deg)}
  .carton-base .mint{position:absolute;right:24px;top:18px;width:110px;height:58px;background:var(--lime);transform:rotate(180deg)}
  .carton-base .mint .tag{position:absolute;left:8px;top:6px;font-weight:700;color:var(--navy);font-size:16px}

  /* ---------- sachets ---------- */
  .sachet{background:var(--paper);border:1px solid #c9d6e3}
  .sachet .head{position:absolute;left:0;right:0;top:0;background:var(--ice);color:var(--navy);text-align:center;font-family:"Archivo Black","Arial Black",sans-serif}
  .sachet .band{position:absolute;left:0;right:0;background:linear-gradient(var(--navy),var(--blue));text-align:center}
  .sachet .band .kicker{display:block;font-size:9px;padding-top:6px}
  .sachet .band .brand{display:block;font-size:34px;margin-top:2px}
  .sachet .tagline{position:absolute;left:0;right:0;background:var(--sky);color:var(--paper);font-size:9px;text-align:center;letter-spacing:1px}
  .sachet .foot{position:absolute;left:0;right:0;bottom:0;height:28px;background:var(--navy)}
  .sachet .foot .url{display:block;text-align:center;font-size:10px;line-height:28px}

  .sachet-front{left:625px;top:24px;width:275px;height:300px}
  .sachet-front .head{height:48px;font-size:20px;line-height:48px}
  .sachet-front .band{top:48px;height:70px}
  .sachet-front .tagline{top:118px;height:20px;line-height:20px}
  .sachet-front .checks{position:absolute;left:16px;top:150px;font-size:10px}
  .sachet-front .diagram{position:absolute;right:16px;top:146px;width:100px;height:100px}
  .sachet-front .dose{position:absolute;left:16px;top:206px;color:var(--lime-dark);font-weight:700;font-size:26px;line-height:1}
  .sachet-front .dose small{display:block;font-size:9px;color:var(--navy)}

  .sachet-back{left:925px;top:24px;width:250px;height:300px}
  .sachet-back .band{top:0;height:62px;text-align:left;padding-left:14px}
  .sachet-back .band .brand{font-size:30px}
  .sachet-back .checks{position:absolute;left:14px;top:70px;font-size:10px}
  .facts{position:absolute;left:14px;right:14px;top:112px;border:1.5px solid var(--ink);padding:4px 6px;font-size:8px;line-height:1.35}
  .facts h3{font-family:"Archivo Black","Arial Black",sans-serif;font-size:12px;border-bottom:3px solid var(--ink);margin-bottom:2px}
  .facts table{width:100%;border-collapse:collapse}
  .facts td{border-top:1px solid var(--ink);padding:1px 0}
  .facts td:last-child{text-align:right}
  .sachet-back .addr{position:absolute;left:14px;right:14px;top:232px;font-size:7.5px;line-height:1.4}

  .sachet-single{left:648px;top:420px;width:312px;height:408px}
  .sachet-single .ribbon{left:-28px;top:6px;width:92px;height:20px;line-height:20px;font-size:11px}
  .sachet-single .band{top:0;height:82px;text-align:right;padding-right:18px}
  .sachet-single .band .kicker{padding-top:10px}
  .sachet-single .band .brand{font-size:36px;margin-top:4px}
  .sachet-single .head{top:82px;height:70px;font-size:24px;padding-top:10px;line-height:1.05;background:var(--paper)}
  .sachet-single .tagline{top:158px;height:24px;line-height:24px;font-size:10px}
  .sachet-single .checks{position:absolute;left:18px;top:200px;font-size:12px}
  .sachet-single .diagram{position:absolute;right:18px;top:196px;width:120px;height:120px}
  .sachet-single .dose{position:absolute;left:18px;top:262px;width:140px;color:var(--lime-dark);font-weight:700;font-size:32px;line-height:1}
  .sachet-single .dose small{display:block;margin-top:4px;font-size:10px;line-height:1.3;color:var(--navy)}
  .sachet-single .foot{height:34px}
  .sachet-single .foot .url{line-height:34px;font-size:11px}
</style>
</head>
<body>

<!-- carton net -->
<section class="piece carton-top">
  <div class="kicker">Dietary Supplement</div>
  <div class="brand">GASTRELLE</div>
  <div class="stripe"></div>
</section>

<section class="piece carton-side">
  <div class="vert"><span class="kicker">Dietary Supplement</span><span class="brand">GASTRELLE</span></div>
  <div class="foot">
    <div class="mint-art" role="img" aria-label="Mint leaves and white tablets"></div>
    <div class="tag">Mint · 5 Packs</div>
  </div>
</section>

<section class="piece front carton-front">
  <div class="ribbon">NEW!</div>
  <div class="band">
    <div class="kicker">Dietary Supplement</div>
    <div class="brand">GASTRELLE</div>
    <div class="count">5 Packs</div>
  </div>
  <div class="tagline caps">Nausea Prevention for Alcohol Use</div>
  <div class="tile">
    <div class="mint-art" role="img" aria-label="Mint leaves with white tablets"></div>
    <div class="tag">Mint</div>
    <div class="note">5 2-tablet packs (10 Tablets)</div>
  </div>
  <div class="proof caps">Clinically<br>Proven</div>
  <div class="checks"><span>✓</span>Protect Stomach<br><span>✓</span>Neutralize Acid</div>
  <div class="diagram" role="img" aria-label="Diagram of a stomach protected by the tablet lining"></div>
  <div class="foot"><div class="url">www.gastrelle.example</div></div>
</section>

<section class="piece carton-base">
  <p class="copy">Directions: take two tablets before drinking. Do not exceed six tablets per day. Keep out of reach of children. Made in USA. Distributed by Quillon Industries LLC, 120 Harbor Way, Ashford, OR 97000. (000) 555-0142</p>
  <div class="mint"><div class="tag">Mint</div></div>
</section>

<section class="piece front carton-back">
  <div class="band">
    <div class="kicker">Dietary Supplement</div>
    <div class="brand">GASTRELLE</div>
    <div class="count">5 Packs</div>
  </div>
  <div class="tagline caps">Nausea Prevention for Alcohol Use</div>
  <div class="tile">
    <div class="mint-art" role="img" aria-label="Mint leaves with white tablets"></div>
    <div class="tag">Mint</div>
  </div>
  <div class="checks"><span>✓</span>Neutralize Acid<br><span>✓</span>Protect Stomach</div>
  <div class="diagram" role="img" aria-label="Diagram of a protected stomach"></div>
  <div class="foot"><div class="url">www.gastrelle.example</div></div>
</section>

<!-- sachet front -->
<section class="piece sachet sachet-front">
  <div class="head caps">Clinically Proven</div>
  <div class="band"><span class="kicker">Dietary Supplement</span><span class="brand">GASTRELLE</span></div>
  <div class="tagline caps">Nausea Prevention for Alcohol Use</div>
  <div class="checks"><span>✓</span>Neutralizes Acid<br><span>✓</span>Protect Stomach</div>
  <div class="dose">2 <small>Tablets · Mint</small></div>
  <div class="diagram" role="img" aria-label="Diagram of a stomach protected by the tablet lining"></div>
  <div class="foot"><span class="url">www.gastrelle.example</span></div>
</section>

<!-- sachet back -->
<section class="piece sachet sachet-back">
  <div class="band"><span class="kicker">Dietary Supplement</span><span class="brand">GASTRELLE</span></div>
  <div class="checks"><span>✓</span>Neutralizes Acid <span>✓</span>Protect Stomach</div>
  <div class="facts">
    <h3>Supplement Facts</h3>
    Serving Size 2 Tablets · Servings 1
    <table>
      <tr><td>Calcium Carbonate</td><td>2000 mg</td></tr>
      <tr><td>Per Tablet</td><td>1000 mg</td></tr>
      <tr><td>Other: mint flavor, sucrose</td><td></td></tr>
    </table>
  </div>
  <p class="addr">Made in USA. Distributed by Quillon Industries LLC, 120 Harbor Way, Ashford, OR 97000</p>
</section>

<!-- single sachet -->
<section class="piece sachet sachet-single">
  <div class="ribbon">NEW!</div>
  <div class="band"><span class="kicker">Dietary Supplement</span><span class="brand">GASTRELLE</span></div>
  <div class="head caps">Clinically<br>Proven</div>
  <div class="tagline caps">Nausea Prevention for Alcohol Use</div>
  <div class="checks"><span>✓</span>Neutralizes Acid<br><span>✓</span>Protect Stomach</div>
  <div class="dose">2 <small>Tablets · 1000mg<br>Calcium Carbonate</small></div>
  <div class="diagram" role="img" aria-label="Diagram of a stomach protected by the tablet lining"></div>
  <div class="foot"><span class="url">www.gastrelle.example</span></div>
</section>

</body>
</html>
```